Copperleaf Motorized Shade Business Card

Hello, we've had our logo made. Now we are looking for a clean and cool looking business card. One side can just be the logo with any design elements that might look good with it. The other side will be Name, Phone Number and Email. There will not be an address on the card.

```html
<!DOCTYPE html>
<html lang="en">
<head>
<meta charset="utf-8">
<title>Copperleaf Motorized Shade – Business Card</title>
<link href="https://fonts.googleapis.com/css2?family=Montserrat:wght@700&family=Lato:wght@400&display=swap" rel="stylesheet">
<style>
  :root {
    --backdrop: #3a3b3d;
    --card-white: #f4f4f2;
    --cream: #f3ecd3;
    --navy: #0e4a86;
    --sun: #f6b511;
    --ink-light: #fdf6e3;
  }
  * { margin: 0; padding: 0; box-sizing: border-box; }
  html, body { width: 1200px; height: 900px; overflow: hidden; }
  body {
    background: var(--backdrop);
    position: relative;
    font-family: "Lato", sans-serif;
  }
  .card {
    position: absolute;
    width: 560px;
    height: 320px;
    background: var(--card-white);
    overflow: hidden;
    box-shadow: 0 12px 28px rgba(0,0,0,.45);
  }
  .card--front { left: 240px; top: 90px; }
  .card--back  { left: 400px; top: 490px; }
  .card__art { position: absolute; inset: 0; width: 100%; height: 100%; }

  .brand {
    position: absolute;
    display: flex;
    align-items: center;
    gap: 14px;
    font-family: "Montserrat", sans-serif;
    font-weight: 700;
    color: var(--navy);
    line-height: 1.1;
    text-transform: uppercase;
    white-space: nowrap;
  }
  .brand__dot {
    flex: none;
    border-radius: 50%;
    background: var(--sun);
  }
  .card--front .brand { left: 110px; top: 118px; font-size: 30px; }
  .card--front .brand__dot { width: 52px; height: 52px; }
  .card--back .brand { left: 30px; top: 132px; font-size: 18px; gap: 12px; }
  .card--back .brand__dot { width: 34px; height: 34px; }

  .contact {
    position: absolute;
    right: 24px;
    top: 78px;
    text-align: right;
    color: var(--navy);
    white-space: nowrap;
  }
  .contact__role { font-size: 15px; color: var(--ink-light); }
  .contact__name { font-size: 19px; letter-spacing: .5px; margin-bottom: 18px; }
  .contact__line {
    font-size: 12.5px;
    color: var(--ink-light);
    margin-top: 8px;
    display: flex;
    justify-content: flex-end;
    align-items: center;
    gap: 6px;
  }
  .contact__icon { width: 12px; height: 12px; fill: var(--navy); flex: none; }
</style>
</head>
<body>

<section class="card card--front" aria-label="Card front">
  <svg class="card__art" viewBox="0 0 560 320" aria-hidden="true">
    <polygon points="0,40 300,0 320,260 0,320" fill="var(--cream)"/>
    <polygon points="60,66 210,40 70,70" fill="#fff"/>
    <polygon points="120,250 330,205 140,256" fill="#fff"/>
    <polygon points="180,302 470,238 200,308" fill="#fff"/>
  </svg>
  <div class="brand">
    <span class="brand__dot"></span>
    <span>Copperleaf<br>Motorized Shade</span>
  </div>
</section>

<section class="card card--back" aria-label="Card back">
  <svg class="card__art" viewBox="0 0 560 320" aria-hidden="true">
    <circle cx="720" cy="150" r="420" fill="var(--sun)"/>
    <polygon points="300,62 560,14 560,22 306,70" fill="var(--card-white)"/>
    <polygon points="296,252 560,208 560,216 302,260" fill="var(--card-white)"/>
    <polygon points="320,304 560,266 560,274 326,312" fill="var(--card-white)"/>
  </svg>
  <div class="brand">
    <span class="brand__dot"></span>
    <span>Copperleaf<br>Motorized Shade</span>
  </div>
  <div class="contact">
    <p class="contact__role">Director</p>
    <p class="contact__name">MARCUS HALE</p>
    <p class="contact__line">(00) 0000 0000
      <svg class="contact__icon" viewBox="0 0 16 16" aria-hidden="true"><path d="M3 1h3l1 4-2 1a9 9 0 0 0 5 5l1-2 4 1v3a2 2 0 0 1-2 2A13 13 0 0 1 1 3a2 2 0 0 1 2-2z"/></svg>
      | 0000 000 000
      <svg class="contact__icon" viewBox="0 0 16 16" aria-hidden="true"><path d="M4 0h8a1 1 0 0 1 1 1v14a1 1 0 0 1-1 1H4a1 1 0 0 1-1-1V1a1 1 0 0 1 1-1zm1 2v10h6V2z"/></svg>
    </p>
    <p class="contact__line">marcus@copperleafshade.com
      <svg class="contact__icon" viewBox="0 0 16 16" aria-hidden="true"><path d="M1 3h14v10H1zm1 1v1l6 4 6-4V4z"/></svg>
    </p>
  </div>
</section>

</body>
</html>
```